Labels for probiotic care products as Body Cream, Shower gel, Hand soap, ....

We are a starting a business in Flanders Belgium. We are looking for a label for care products, based on probiotics or good bacterie. We are looking for a fresh design that attracts people who wants a good product, based on naturally components. The products make that the microflora of the skin becomes and remains natural. The label must we be adaptive on bottles of 15 cm height to 8 cm height and a width of 4,5 cm. The brand name is KOLA EMU (beautiful skin in Hawaiian) or maybe just KOLA.

Industry/Entity Type

Business

Colors

Designer to choose colors to be used in the design.

Requirements
Must have
• somewhere the text "Probiotic Skin Care"
• I also have to tell that the bottles are white.
Nice to have
• I uploaded the 9 existing labels, but I want a totally new one, because the labels of our cleaning products are the same. I also uploaded a mood bord of labels I like.

```html
<!DOCTYPE html>
<html lang="en">
<head>
<meta charset="utf-8">
<title>KOLA EMU – Skin Repair Label</title>
<link rel="stylesheet" href="https://fonts.googleapis.com/css2?family=Montserrat:wght@400;500&display=swap">
<style>
  :root {
    --page-bg: #f4f4f4;
    --label-white: #ffffff;
    --teal: #1a8e95;
    --teal-deep: #127980;
    --slate: #6f7b7c;
    --brand-grey: #5f7677;
    --text-light: #ffffff;
  }
  html, body {
    margin: 0;
    padding: 0;
    width: 900px;
    height: 1200px;
    overflow: hidden;
    background: var(--page-bg);
    font-family: "Montserrat", sans-serif;
  }
  .canvas {
    position: relative;
    width: 900px;
    height: 1200px;
  }
  .label {
    position: absolute;
    left: 210px;
    top: 25px;
    width: 480px;
    height: 1150px;
    background: var(--label-white);
    box-shadow: 0 2px 12px rgba(0,0,0,0.08);
    overflow: hidden;
  }
  .pattern-band {
    position: absolute;
    left: 0;
    top: 0;
    width: 100%;
    height: 338px;
    background: linear-gradient(180deg, var(--teal) 0%, var(--teal-deep) 100%);
  }
  .brand-name {
    position: absolute;
    left: 0;
    width: 100%;
    top: 455px;
    text-align: center;
    font-weight: 400;
    font-size: 54px;
    letter-spacing: 6px;
    color: var(--brand-grey);
    margin: 0;
  }
  .bubble-mark {
    position: absolute;
    left: 50%;
    top: 714px;
    transform: translateX(-50%);
    width: 120px;
    height: 120px;
  }
  .product-name {
    position: absolute;
    left: 77px;
    top: 858px;
    width: 300px;
    height: 68px;
    background: var(--slate);
    color: var(--text-light);
    display: flex;
    align-items: center;
    justify-content: center;
    font-weight: 500;
    font-size: 30px;
    letter-spacing: 3px;
    margin: 0;
  }
  .product-info {
    position: absolute;
    left: 77px;
    top: 926px;
    width: 300px;
    height: 224px;
    background: var(--teal);
    color: var(--text-light);
    text-align: center;
  }
  .tagline {
    margin: 30px 0 0;
    font-size: 23px;
    font-weight: 500;
  }
  .divider {
    width: 82px;
    height: 1px;
    background: var(--text-light);
    opacity: 0.8;
    margin: 50px auto 0;
  }
  .volume {
    margin: 28px 0 0;
    font-size: 21px;
  }
</style>
</head>
<body>
  <main class="canvas">
    <section class="label">
      <div class="pattern-band" role="img" aria-label="Teal band with a repeating geometric line pattern"></div>

      <h1 class="brand-name">KOLA EMU</h1>

      <svg class="bubble-mark" viewBox="0 0 120 120" role="img" aria-label="Round cluster of small bubbles suggesting good bacteria">
        <circle cx="60" cy="60" r="56" fill="#6f7b7c"/>
      </svg>

      <h2 class="product-name">SKIN REPAIR</h2>
      <div class="product-info">
        <p class="tagline">Probiotic Skin Care</p>
        <div class="divider"></div>
        <p class="volume">℮ 100 ml</p>
      </div>
    </section>
  </main>
</body>
</html>
```